Velmar Ops Business Cards

We need to design some upbeat business cards. We are an Industrial Rope Access Company/Height Safety Company that specialize in Rope Access, Confined Space, Anchor Points, Safety Systems, PPE Inspecions and Rigging.
Company name is Velmar Ops Ltd
Card is for Gareth Lomas the Company Director
His mobile number is 027 418 9072 and email is gareth@velmarops.co.nz. Website address is www.velmarops.co.nz.
We will post some pictures below to ensure you get a good idea of what we do.

```html
<!DOCTYPE html>
<html lang="en">
<head>
<meta charset="utf-8">
<title>Velmar Ops — Business Cards</title>
<link rel="stylesheet" href="https://fonts.googleapis.com/css2?family=Bebas+Neue&family=Work+Sans:wght@400;500;800&family=Roboto:wght@400&display=swap">
<style>
  :root {
    --backdrop: #e6e6e6;
    --navy: #221f52;
    --white: #ffffff;
    --rule-blue: #3d56a8;
    --on-navy: #ffffff;
    --muted-on-navy: #d4d4e2;
  }
  * { margin: 0; padding: 0; box-sizing: border-box; }
  html, body {
    width: 1200px; height: 897px; overflow: hidden;
    background: var(--backdrop);
  }
  .card {
    position: absolute; left: 303px; width: 595px; height: 339px;
    overflow: hidden;
  }
  .card--front { top: 92px; background: var(--white); }
  .card--back { top: 469px; background: var(--navy); }

  .wordmark {
    position: absolute; left: 0; right: 0; text-align: center;
    font-family: "Work Sans", sans-serif; font-weight: 800;
    font-size: 50px; letter-spacing: 0.5px; line-height: 1;
  }
  .card--front .wordmark { top: 75px; color: var(--navy); }
  .card--back .wordmark { top: 142px; color: var(--muted-on-navy); }

  .front-rule {
    position: absolute; left: 0; right: 0; top: 198px; height: 2px;
    background: var(--rule-blue);
  }
  .front-band {
    position: absolute; left: 0; right: 0; top: 204px; bottom: 0;
    background: var(--navy);
  }
  .holder {
    position: absolute; right: 343px; top: 45px; text-align: right;
    color: var(--on-navy);
  }
  .holder__name {
    font-family: "Bebas Neue", sans-serif; font-size: 38px;
    line-height: 1; letter-spacing: 0.5px;
  }
  .holder__role {
    font-family: "Work Sans", sans-serif; font-size: 14px; line-height: 1.2;
  }
  .divider {
    position: absolute; left: 273px; top: 45px; width: 2px; height: 47px;
    background: var(--on-navy);
  }
  .contacts {
    position: absolute; left: 298px; top: 40px; list-style: none;
    font-family: "Work Sans", sans-serif; font-size: 15px; color: var(--on-navy);
  }
  .contacts li { display: flex; align-items: center; height: 19px; }
  .contacts svg { width: 9px; height: 9px; margin-right: 9px; flex: none; }

  .services {
    position: absolute; left: 0; right: 0; top: 272px; text-align: center;
    font-family: "Roboto", sans-serif; font-size: 14px; line-height: 21px;
    color: var(--muted-on-navy);
  }
</style>
</head>
<body>
  <section class="card card--front">
    <div class="wordmark">Velmar Ops</div>
    <div class="front-rule"></div>
    <div class="front-band">
      <div class="holder">
        <div class="holder__name">GARETH LOMAS</div>
        <div class="holder__role">Director</div>
      </div>
      <div class="divider"></div>
      <ul class="contacts">
        <li>
          <svg viewBox="0 0 10 10" fill="none" stroke="#fff" stroke-width="1.3"><path d="M2 1 L4 1 L4.6 3.4 L3.4 4.2 Q4.5 6.2 6 6.8 L6.8 5.6 L9 6.2 L9 8.4 Q5 9 2.5 6 Q1 4 2 1 Z"/></svg>
          027 418 9072
        </li>
        <li>
          <svg viewBox="0 0 10 10" fill="none" stroke="#fff" stroke-width="1.2"><rect x="0.8" y="2" width="8.4" height="6"/><path d="M0.8 2 L5 5.4 L9.2 2"/></svg>
          gareth@velmarops.co.nz
        </li>
        <li>
          <svg viewBox="0 0 10 10" fill="none" stroke="#fff" stroke-width="1"><circle cx="5" cy="5" r="4.2"/><ellipse cx="5" cy="5" rx="1.8" ry="4.2"/><path d="M0.8 5 H9.2"/></svg>
          www.velmarops.co.nz
        </li>
      </ul>
    </div>
  </section>

  <section class="card card--back">
    <div class="wordmark">Velmar Ops</div>
    <p class="services">
      ROPE ACCESS - CONFINED SPACE - ANCHOR POINTS<br>
      SAFETY SYSTEMS - PPE INSPECIONS - RIGGING.
    </p>
  </section>
</body>
</html>
```